Garlic Farm for Farm Sales/Restaurant sales

Need a professional, but appealing to agriculture world. We are selling 27 kinds of Organic Garlic from a farm in Simla,CO. I have uploaded logo and business information-we are going to need a template, because I will need to use it for four separate people.
-We are trying to appeal to Farm to table restaurants
-As well as growers/farmers

Target Market(s)

Agriculture Sales/Restaurants-Organic

Industry/Entity Type

Agriculture

Contact Information for Business Card

Want it to look more unique then your average orbel mart card- I want it to look amazing

Font styles to use
Sans Serif

Colors
0455a3
ec1f27
fbed22
ffffff

Requirements
Must have
• Just be creative
Nice to have
• Colorful
Should not have
• plain

```html
<!DOCTYPE html>
<html lang="en">
<head>
<meta charset="utf-8">
<title>Plainsbulb Farm — Business Card</title>
<link href="https://fonts.googleapis.com/css2?family=Source+Sans+3:ital,wght@0,400;0,600;1,400;1,700&display=swap" rel="stylesheet">
<style>
  :root {
    --brand-red: #c8102e;
    --brand-blue: #0455a3;
    --brand-yellow: #fbdc00;
    --card-white: #ffffff;
    --ink: #1e1e1e;
    --page-bg: #e9e7e4;
    --seam-light: #f1f1f1;
    --seam-dark: #c9c6c3;
  }
  * { box-sizing: border-box; margin: 0; padding: 0; }
  html, body {
    width: 1200px; height: 900px; overflow: hidden;
    background: var(--page-bg);
    font-family: "Source Sans 3", "Myriad Pro", Arial, sans-serif;
  }
  .business-card {
    position: absolute; left: 150px; top: 171px;
    width: 900px; height: 558px;
    background: var(--card-white);
    overflow: hidden;
    box-shadow: 0 10px 30px rgba(0,0,0,0.15);
  }
  .accent-band {
    position: absolute; top: 0; right: 0; bottom: 0; width: 261px;
    background: var(--brand-yellow);
  }
  .accent-seam {
    position: absolute; top: 0; bottom: 0; left: 620px; width: 19px;
    background: linear-gradient(to right, var(--seam-light), var(--seam-dark));
  }
  .person-name {
    position: absolute; left: 52px; top: 52px;
    font-size: 46px; font-weight: 700; font-style: italic;
    color: var(--brand-red); line-height: 1; letter-spacing: 0.2px;
  }
  .person-role {
    position: absolute; left: 52px; top: 116px;
    font-size: 29px; font-style: italic; color: var(--ink); line-height: 1;
  }
  .contact-list {
    position: absolute; left: 52px; top: 224px; list-style: none;
  }
  .contact-list li {
    display: flex; align-items: center; height: 36.5px;
    font-size: 27px; color: var(--ink);
  }
  .contact-list svg { width: 24px; height: 24px; margin-right: 11px; fill: var(--brand-red); flex: none; }
  .postal-address {
    position: absolute; left: 52px; top: 444px;
    font-size: 27px; line-height: 36px; color: var(--ink); font-style: normal;
  }
  .farm-mark {
    position: absolute; left: 473px; top: 95px; width: 320px;
    display: flex; flex-direction: column; align-items: center;
  }
  .farm-mark-dot {
    width: 230px; height: 230px; border-radius: 50%;
    background: var(--brand-red);
  }
  .farm-mark-name {
    margin-top: 22px;
    font-size: 36px; font-weight: 600; color: var(--brand-blue); white-space: nowrap;
  }
</style>
</head>
<body>
  <div class="business-card">
    <div class="accent-band"></div>
    <div class="accent-seam"></div>

    <h1 class="person-name">dara wells</h1>
    <p class="person-role">Owner</p>

    <ul class="contact-list">
      <li>
        <svg viewBox="0 0 24 24" aria-hidden="true"><path d="M2 9c0-3 5-5 10-5s10 2 10 5v2h-5V9c-2-1-8-1-10 0v2H2z M6 12h12l2 8H4z M12 14a2.5 2.5 0 1 0 0.01 0z"/></svg>
        <span>555-014-2287</span>
      </li>
      <li>
        <svg viewBox="0 0 24 24" aria-hidden="true"><path d="M7 2h10v5H7z M3 8h18v14H3z M6 11v3h12v-3z M6 16h3v2H6z M10.5 16h3v2h-3z M15 16h3v2h-3z"/></svg>
        <span>(555)-019-4</span>
      </li>
      <li>
        <svg viewBox="0 0 24 24" aria-hidden="true"><path d="M2 5h20v14H2z" /><path d="M2 5l10 8 10-8" fill="none" stroke="#fff" stroke-width="2"/></svg>
        <span>hello@plainsbulb.com</span>
      </li>
      <li>
        <svg viewBox="0 0 24 24" aria-hidden="true"><circle cx="12" cy="12" r="10"/><path d="M7 7c2 0 3 1 3 3s-2 2-2 4 1 3 1 5M15 4c0 2 1 3 3 3M16 13c1 0 2 1 2 3" fill="none" stroke="#fff" stroke-width="1.8"/></svg>
        <span>www.plainsbulb.com</span>
      </li>
    </ul>

    <address class="postal-address">PO Box 318,<br>Simla, CO 80835</address>

    <div class="farm-mark">
      <div class="farm-mark-dot"></div>
      <p class="farm-mark-name">Plainsbulb Farm</p>
    </div>
  </div>
</body>
</html>
```